Book Cover needed for Printed Book entitled "Step 7"

The Book's Title is "Step 7", the sub-title is "One Resident's Manual on Calm Roadside Stops by Patrol Units", and the author is "Desmond Okafor". The front cover may have just the Title, or it may have a combination of the Title, Sub-Title, and Author. We would like to see designs that presents a feeling of peace and cooperation between US Police Officers and Civilians. The cover can include photographs, illustrations, or just words. But the cover should make the viewer want to open the book for more information.

Target Market(s)

Young adults who live in US inner-cities between ages 18 to 30.

Font styles to use
Sans Serif

Colors

Designer to choose colors to be used in the design.

Requirements
Must have
• Most US Police Officers use the phrase "STEP 7" to tell other officers that the situation is under control and no assistance is needed. And the book will teach Civilians how to safely conduct themselves during police encounters - which will end with the Cops calling in "STEP 7" to the dispatcher. So, the front cover must have the phrase "STEP 7" in big bold letters.
Nice to have
• We would like to see designs that present a feeling of peace and cooperation between US Police Officers and Civilians. Pictures and illustrations of people are acceptable but is not required.

```html
<!DOCTYPE html>
<html lang="en">
<head>
<meta charset="utf-8">
<title>Step 7 — Book Cover</title>
<link rel="stylesheet" href="https://fonts.googleapis.com/css2?family=Bebas+Neue&family=Oswald:wght@500;600&display=swap">
<style>
  :root {
    --sky-deep: #14307a;
    --sky-mid: #1a56a6;
    --sky-light: #2a86cf;
    --navy: #2a3a7c;
    --flag-red: #c1272d;
    --paper: #ffffff;
  }
  html, body {
    margin: 0;
    padding: 0;
    overflow: hidden;
    background: var(--paper);
  }
  .cover {
    position: relative;
    width: 800px;
    height: 1200px;
    overflow: hidden;
    background: var(--paper);
  }
  .cover-art {
    position: absolute;
    inset: 0;
    width: 800px;
    height: 1200px;
  }
  .title {
    position: absolute;
    top: 62px;
    left: 0;
    width: 800px;
    margin: 0;
    text-align: center;
    font-family: "Bebas Neue", sans-serif;
    font-weight: 400;
    font-size: 372px;
    line-height: 1;
    letter-spacing: 6px;
    color: var(--paper);
  }
  .subtitle {
    position: absolute;
    top: 716px;
    left: 124px;
    width: 620px;
    margin: 0;
    font-family: "Oswald", sans-serif;
    font-weight: 600;
    font-size: 54px;
    line-height: 76px;
    letter-spacing: -0.5px;
    color: var(--navy);
  }
  .subtitle .accent { color: var(--flag-red); }
  .subtitle span.line { display: block; white-space: nowrap; }
  .author-band {
    position: absolute;
    top: 1092px;
    left: 0;
    width: 800px;
    height: 60px;
    background: var(--navy);
    display: flex;
    align-items: center;
    justify-content: center;
  }
  .author {
    font-family: "Oswald", sans-serif;
    font-weight: 500;
    font-size: 40px;
    letter-spacing: 1px;
    color: var(--paper);
  }
</style>
</head>
<body>
  <div class="cover">
    <svg class="cover-art" viewBox="0 0 800 1200" xmlns="http://www.w3.org/2000/svg">
      <defs>
        <radialGradient id="sky" cx="0.5" cy="0.72" r="0.75">
          <stop offset="0" stop-color="var(--sky-light)"/>
          <stop offset="0.55" stop-color="var(--sky-mid)"/>
          <stop offset="1" stop-color="var(--sky-deep)"/>
        </radialGradient>
        <linearGradient id="ribbon" x1="0" y1="0" x2="0" y2="1">
          <stop offset="0" stop-color="#2a4a96"/>
          <stop offset="0.45" stop-color="#f2f2f4"/>
          <stop offset="1" stop-color="#c1272d"/>
        </linearGradient>
      </defs>
      <path class="sky-field" d="M0,0 H800 V452 C640,448 520,470 400,505 C270,545 140,568 0,572 Z" fill="url(#sky)"/>
      <path class="flag-ribbon" role="img" aria-label="Waving stars-and-stripes ribbon in red, white and blue"
            d="M0,572 C140,568 270,545 400,505 C520,470 640,448 800,452 V478 C650,478 540,505 430,548 C300,598 150,615 0,616 Z"
            fill="url(#ribbon)"/>
    </svg>

    <h1 class="title">STEP 7</h1>

    <p class="subtitle">
      <span class="line">One Resident's <span class="accent">Manual</span></span>
      <span class="line">on Calm <span class="accent">Roadside Stops</span></span>
      <span class="line accent">by Patrol Units</span>
    </p>

    <div class="author-band">
      <span class="author">Desmond Okafor</span>
    </div>
  </div>
</body>
</html>
```